Brevik Electric Business Card

An electrical contractor needs a business card design, that will stand out.
I would like designs that use the colors in the logo shown. The logo attached I am ok with but if you have a better idea I am open for suggestions. I like the color scheme.
Industry/Entity Type
Electrical
Contact Information for Business Card
Services, social media, QR code,

```html
<!DOCTYPE html>
<html lang="en">
<head>
<meta charset="utf-8">
<title>Brevik Electric Business Card</title>
<link rel="stylesheet" href="https://fonts.googleapis.com/css2?family=Montserrat:wght@700&family=Open+Sans:wght@400;600;700&display=swap">
<style>
  :root {
    --bg: #3d3d3d;
    --card-light: #fbfbfb;
    --card-dark: #161616;
    --ink: #1c1c1c;
    --ink-soft: #555555;
    --accent: #f0b623;
    --white: #ffffff;
    --rule: #9a9a9a;
  }
  * { box-sizing: border-box; margin: 0; padding: 0; }
  html, body { width: 1200px; height: 801px; overflow: hidden; }
  body {
    background: var(--bg);
    font-family: "Open Sans", Arial, sans-serif;
    display: flex;
    align-items: center;
    justify-content: center;
    gap: 60px;
  }
  .card {
    width: 525px;
    height: 300px;
    position: relative;
    box-shadow: 0 10px 30px rgba(0,0,0,.35);
  }
  .card--front { background: var(--card-light); }
  .card--back {
    background: var(--card-dark);
    display: flex;
    align-items: center;
    justify-content: center;
  }
  .identity {
    position: absolute;
    right: 300px;
    top: 96px;
    text-align: right;
  }
  .identity__name {
    font-weight: 700;
    font-size: 19px;
    color: var(--ink);
    letter-spacing: .3px;
    text-transform: uppercase;
  }
  .identity__title {
    font-weight: 600;
    font-size: 14px;
    color: var(--accent);
  }
  .divider {
    position: absolute;
    left: 240px;
    top: 78px;
    width: 1px;
    height: 70px;
    background: var(--rule);
  }
  .contacts {
    position: absolute;
    left: 256px;
    top: 80px;
    list-style: none;
  }
  .contacts__item {
    display: flex;
    align-items: center;
    gap: 7px;
    font-size: 13px;
    color: var(--ink-soft);
    line-height: 22px;
  }
  .contacts__icon { width: 11px; height: 11px; flex: none; }
  .address {
    position: absolute;
    left: 0;
    right: 0;
    bottom: 58px;
    text-align: center;
    font-size: 14px;
    color: var(--ink-soft);
  }
  .brand {
    display: flex;
    align-items: center;
    gap: 16px;
  }
  .brand__mark {
    width: 40px;
    height: 40px;
    background: var(--accent);
  }
  .brand__name {
    font-family: "Montserrat", Arial, sans-serif;
    font-weight: 700;
    font-size: 32px;
    color: var(--white);
    letter-spacing: .5px;
    text-transform: uppercase;
  }
</style>
</head>
<body>
  <section class="card card--front">
    <div class="identity">
      <p class="identity__name">Daren Holloway</p>
      <p class="identity__title">President</p>
    </div>
    <div class="divider"></div>
    <ul class="contacts">
      <li class="contacts__item">
        <svg class="contacts__icon" viewBox="0 0 12 12"><path fill="#f0b623" d="M2.4 0.8 4.2 0.5 5 3.1 3.7 4.1Q4.6 6.6 7.6 8.2L8.7 7 11.3 7.9 11 9.8Q9.9 11.6 7.4 10.6 2.1 8.3 1 3.3 0.9 1.6 2.4 0.8Z"/></svg>
        555-014-2290
      </li>
      <li class="contacts__item">
        <svg class="contacts__icon" viewBox="0 0 12 12"><rect x="0.5" y="2" width="11" height="8" rx="1" fill="#f0b623"/><path d="M1 2.8 6 6.6 11 2.8" fill="none" stroke="#fbfbfb" stroke-width="1"/></svg>
        dholloway@BrevikElectric.com
      </li>
      <li class="contacts__item">
        <svg class="contacts__icon" viewBox="0 0 12 12"><circle cx="6" cy="6" r="5.5" fill="#f0b623"/><path d="M0.8 6H11.2M6 0.5Q3 6 6 11.5M6 0.5Q9 6 6 11.5" fill="none" stroke="#fbfbfb" stroke-width=".8"/></svg>
        www.BrevikElectric.com
      </li>
    </ul>
    <p class="address">1830 Harbor Lane, Seacliff CA 92000</p>
  </section>

  <section class="card card--back">
    <div class="brand">
      <span class="brand__mark"></span>
      <span class="brand__name">Brevik Electric</span>
    </div>
  </section>
</body>
</html>
```